Business Card Design

My company is a health food catering and delivery business. Our colours are a bright turquiose green/blue, black, white and natural brown based beige. I would like the front of my card (working from the outside in; with a turquoise green boarder -quite thick, with a thin black line separating the turquoise boarder from the beige inside the remaining space of the front of the card with my logo in the centre. This should be all that appears on the front.

On the back I would like all the information displayed above on the beige coloured card, with the blurb in the bright turquoise and my contact information in black please. I would like my business name central - Harvest Lantern Kitchen and immediately below with a right alignment - ...Dine with Delight
Below this should follow all that I have displayed above with a left alignment.

Target Market(s)

Cafes, restaurants, individuals, buying agents & super markets

Industry/Entity Type

Catering

Contact Information for Business Card

BACK OF BUSINESS CARD:
Harvest Lantern Kitchen
...Dine with Delight
Deliciously healthy foods - free from gluten, lactose, cane sugar, trans-fat, GMO corn, soy & rice, no artificial flavours, colours or preservatives.
Prepared fresh from locally sourced ingredients, delivered to your door! For individuals, families, corporate, cafes, restaurants & event catering for Toowoomba & surrounds!

PH: 0491 382 907 // orders@harvestlanternkitchen.example
www.harvestlanternkitchen.example
www.social.example/harvestlanternkitchen

Requirements
Must have
• Please supply a modern, easy to read text that will blend nicely with my logo text.
Nice to have
• I really want my business cards to stand out as these will be the template for brochures, menus and website designers to draw inspiration from!
Should not have
• Please do not use Arial, Tahoma or Times Roman text.

```html
<!DOCTYPE html>
<html lang="en">
<head>
<meta charset="utf-8">
<title>Harvest Lantern Kitchen – Business Card</title>
<link href="https://fonts.googleapis.com/css2?family=Courgette&family=Varela+Round&display=swap" rel="stylesheet">
<style>
  :root {
    --stage: #231f20;
    --card-white: #ffffff;
    --turquoise: #29a7df;
    --ink: #1a1a1a;
    --beige: #ecdcb3;
    --cream: #f7f2e6;
    --sand: #e8d3a6;
  }
  * { box-sizing: border-box; margin: 0; padding: 0; }
  html, body {
    width: 1200px; height: 846px; overflow: hidden;
    background: var(--stage);
  }
  .canvas { position: relative; width: 1200px; height: 846px; }

  .card {
    position: absolute;
    width: 540px; height: 330px;
    border-radius: 26px;
  }

  /* Front */
  .card--front {
    left: 70px; top: 80px;
    background: var(--card-white);
    padding: 18px;
  }
  .front-border {
    width: 100%; height: 100%;
    border: 9px solid var(--turquoise);
    border-radius: 14px;
    padding: 5px;
    background: var(--card-white);
  }
  .front-inner {
    width: 100%; height: 100%;
    border: 1.5px solid var(--ink);
    border-radius: 8px;
    background: var(--cream);
    display: flex; flex-direction: column; align-items: center; justify-content: center;
    gap: 6px;
  }
  .logo-art {
    width: 250px; height: 150px;
    border-radius: 6px;
    background: radial-gradient(ellipse at center, #ffffff 0%, #f1ead9 60%, var(--sand) 100%);
  }
  .logo-name {
    font-family: "Courgette", cursive;
    font-size: 30px;
    color: var(--ink);
  }

  /* Back */
  .card--back {
    left: 590px; top: 430px;
    background: var(--beige);
    padding: 26px 24px 24px;
    display: flex; flex-direction: column;
  }
  .blurb {
    font-family: "Courgette", cursive;
    font-size: 13.5px;
    line-height: 1.35;
    color: var(--turquoise);
    padding: 0 6px;
  }
  .brand { margin: 14px auto 0; width: 270px; }
  .brand-name {
    font-family: "Courgette", cursive;
    font-size: 25px;
    color: var(--turquoise);
    text-align: center;
    white-space: nowrap;
  }
  .brand-tagline {
    font-family: "Courgette", cursive;
    font-size: 13px;
    color: var(--turquoise);
    text-align: right;
    margin-top: -4px;
  }
  .contacts {
    margin-top: auto;
    display: flex; align-items: stretch;
    color: var(--ink);
    max-width: 100%;
  }
  .contact-col { display: flex; flex-direction: column; gap: 14px; justify-content: center; flex: none; }
  .contact-col--left { padding-right: 12px; border-right: 1px solid var(--ink); }
  .contact-col--right { padding-left: 12px; }
  .contact-item { display: flex; align-items: center; gap: 7px; white-space: nowrap; }
  .contact-item svg { width: 13px; height: 13px; flex: none; }
  .contact-text--sans { font-family: "Varela Round", sans-serif; font-size: 10.5px; }
  .contact-text--phone { font-size: 14px; letter-spacing: 0.5px; }
  .contact-text--script { font-family: "Courgette", cursive; font-size: 10px; }
</style>
</head>
<body>
<main class="canvas">

  <section class="card card--front" aria-label="Card front">
    <div class="front-border">
      <div class="front-inner">
        <div class="logo-art" role="img" aria-label="Logo illustration of a chef holding a whisk and a frying pan"></div>
        <div class="logo-name">Harvest Lantern Kitchen</div>
      </div>
    </div>
  </section>

  <section class="card card--back" aria-label="Card back">
    <p class="blurb">Deliciously healthy foods - free from gluten, lactose, cane sugar, trans-fat, GMO corn, soy &amp; rice, no artificial flavours, colours or preservatives. Prepared fresh from locally sourced ingredients, delivered to your door! For individuals, families, corporate, cafes, restaurants &amp; event catering for Toowoomba &amp; surrounds!</p>

    <div class="brand">
      <div class="brand-name">Harvest Lantern Kitchen</div>
      <div class="brand-tagline">...Dine with Delight</div>
    </div>

    <div class="contacts">
      <div class="contact-col contact-col--left">
        <div class="contact-item">
          <svg viewBox="0 0 14 14" aria-hidden="true"><rect width="14" height="14" rx="3" fill="#1a1a1a"/><path d="M4 3.2c.5-.3 1-.2 1.3.3l.7 1.2c.2.4.1.8-.2 1l-.5.4c.4 1 1.1 1.7 2.1 2.1l.4-.5c.3-.3.7-.4 1-.2l1.2.7c.5.3.6.8.3 1.3-.6.9-1.5 1.2-2.4.8C6 9.6 4.4 8 3.7 6c-.4-.9-.1-1.9.3-2.8z" fill="#ecdcb3"/></svg>
          <span class="contact-text--sans contact-text--phone">0491 382 907</span>
        </div>
        <div class="contact-item">
          <svg viewBox="0 0 14 14" aria-hidden="true"><rect x="1" y="3" width="12" height="8.5" rx="1" fill="none" stroke="#1a1a1a" stroke-width="1.4"/><path d="M1.5 3.6 7 8l5.5-4.4" fill="none" stroke="#1a1a1a" stroke-width="1.4"/></svg>
          <span class="contact-text--sans">orders@harvestlanternkitchen.example</span>
        </div>
      </div>
      <div class="contact-col contact-col--right">
        <div class="contact-item">
          <svg viewBox="0 0 14 14" aria-hidden="true"><rect width="14" height="14" rx="2" fill="#1a1a1a"/></svg>
          <span class="contact-text--script">www.social.example/harvestlanternkitchen</span>
        </div>
        <div class="contact-item">
          <svg viewBox="0 0 14 14" aria-hidden="true"><circle cx="7" cy="7" r="6" fill="none" stroke="#1a1a1a" stroke-width="1.4"/><ellipse cx="7" cy="7" rx="2.6" ry="6" fill="none" stroke="#1a1a1a" stroke-width="1"/><path d="M1 7h12" stroke="#1a1a1a" stroke-width="1"/></svg>
          <span class="contact-text--script">www.harvestlanternkitchen.example</span>
        </div>
      </div>
    </div>
  </section>

</main>
</body>
</html>
```